Maison Orélie is a premium domestic placement company and a concept of modern etiquette and a manueri

Maison Orélie is a premium domestic placements agency delivering the most professional caliber of domestic professionals to suit even the most demanding, challenging and refined household tasks.

Based in Dubai, Maison Orélie the world of Maison Orélie is representing the finest.

We genuinely strive to find the best, recruit the right ones and invest our time and resources for that perfect match.

~ Career Nannies ~
~ Etiquette Governesses ~
~ Royal Protocol Attendees ~
~ Formal Palace Personnel ~
~ Official Butler ~
~ World Class Chefs ~
~ Skilled Housekeepers ~
~ Experienced Babynurses ~
~ Domestic Couples ~
~ Professional Laundresses ~
~ Personal Beautician ~
~ Enthusiastic Chauffeurs ~
~ Gourmet Cooks ~

WEB SITE BRIEF:

Style: clean, classy, refined and screaming luxury - you may see sample i like: www.lunabrevanhouse.example

Colors: I like black and white with a touch of pink (burned sugar more specifically)

Communicate: The images and the web should communicate class and royalty as i will be working with lots of royal families in the Region.

Images selection: this is very important to me has to be with white, black, and perhaps a touch of pink - just to get along with my logo second line.
1. one image may be a palace
2. may be a housekeeper or a butler
3. something etiquette related! or your
PS. Do not limit to those, its just mine idea and also i don't know why but i prefer images without faces - otherwise looks like endorsement and strong personalization to a face that i dont even know

Note: The pictures i have attached are tentative only

Explanation of my web structure: 1 excel page are the web links 2 are the side links, i want them to be like a sliding tips, that you click to see the next 3 social media i will start with

Standards: You may use my logo (middle icon) as a graphic idea and/or whatever you decide i like consistency - in the colors you use, style and all.

General: Easy to navigate

Thank you all in advance & Enjoy the journey

Marguerite

Target Market(s)

- Royal families and VIP's in Middle East
- Families and families with kids
- Mid and High-end segment singles
- Hotels HR departments
- Companies HR departments
- Celebrities ;)

Industry/Entity Type

It Company

Requirements
Must have
• Standards again of design, i don't like mixed style of photography and drawing and sketches all in one. Think there should be an idea in the backbone
Nice to have
• Clean, i like simple things in life
• Elegant and luxury, reliability and care - that should be the message
• on the MAIN side might have one banner that shows my value added package VIP Maison Orélie consisted of the following:
• - priority served contract
• - draw from the best candidates
• - dedicated consultant
• - FREE couture uniform
• - meeting at your choice
• - FREE training from the Maison Orélie advanced manual
• - FREE cooking book
• - Follow up visit/call
Should not have
• 1. variety of styles as said
• 2. images that are used from others in the same industry and styles
• 3. very big letters - prefer smaller fonts
• 4. illustrations that look cheap

```html
<!DOCTYPE html>
<html lang="en">
<head>
<meta charset="utf-8">
<title>Maison Orélie — Premium Domestic</title>
<link rel="stylesheet" href="https://fonts.googleapis.com/css2?family=Lato:wght@300;400&family=Lora:ital@0;1&family=Cinzel&family=Cormorant+Garamond:wght@400&family=Pinyon+Script&display=swap">
<style>
:root{
  --red:#bf302b;
  --red-line:#d2605b;
  --pink:#d77e78;
  --ink:#444;
  --grey:#8a8a8a;
  --light:#b0b0b0;
  --pale:#f2f2f2;
  --line:#cfcfcf;
  --dark:#666;
  --white:#fff;
}
*{box-sizing:border-box;margin:0;padding:0}
html,body{width:979px;height:1200px;overflow:hidden;background:var(--white)}
body{position:relative;font-family:"Lato",sans-serif;color:var(--ink)}
.abs{position:absolute}

.shortlist-bar{left:287px;top:0;width:692px;height:28px;background:var(--pale);display:flex;align-items:center;font-family:"Lora",serif;font-size:10.5px;color:var(--ink)}
.shortlist-bar .label{margin-left:290px}
.shortlist-bar .email{margin-left:14px;width:128px;height:17px;background:var(--white);font-style:italic;font-size:9.5px;color:var(--light);text-align:center;line-height:17px}
.shortlist-bar .social{margin-left:36px;display:flex;gap:9px}
.shortlist-bar .social span{width:10px;height:10px;border-radius:50%;background:#9a9a9a}

.main-nav{left:287px;top:38px;width:642px;display:flex;justify-content:space-between;font-weight:300;font-size:12px;letter-spacing:.3px;color:#6b6b6b}

.brand{left:50px;top:50px;width:190px;text-align:center}
.brand .mark{width:62px;height:62px;border:1px solid var(--light);border-radius:50%;margin:0 auto 44px}
.brand .name{font-family:"Cormorant Garamond",serif;font-size:29px;letter-spacing:1.5px;color:#555;line-height:1}
.brand .sub{font-size:10.5px;letter-spacing:1.6px;color:var(--pink);margin-top:6px}

.tagline{left:287px;top:118px;width:645px;text-align:center;font-family:"Pinyon Script",cursive;font-size:19px;line-height:31px;color:#aaa}

.hero{left:51px;top:258px;width:877px;height:257px;background:linear-gradient(180deg,#bcd3ea 0%,#e3e6e0 30%,#efe2bd 55%,#e6d7b2 78%,#9a8a6a 100%)}
.hero .blooms{position:absolute;right:0;top:0;width:200px;height:257px;background:linear-gradient(90deg,rgba(210,60,90,0),rgba(200,50,80,.55))}

.seeking{left:51px;top:542px;width:678px;height:112px;border:1px solid var(--line);text-align:center}
.seeking h2{font-weight:300;font-size:14.5px;letter-spacing:.8px;color:var(--light);margin-top:16px}
.seeking ul{list-style:none;margin-top:9px;font-weight:300;font-size:10.5px;color:#777;line-height:17px}
.seeking li{display:inline}
.seeking li+li::before{content:"|";color:var(--pink);margin:0 6px}

.card{top:661px;width:222px;height:338px;border:1px solid var(--line);text-align:center}
.card h2{font-family:"Lora",serif;font-weight:400;font-size:15px;color:var(--light);letter-spacing:.5px;margin-top:12px}
.card .btn{position:absolute;left:13px;right:13px;bottom:13px;height:24px;background:var(--pale);font-weight:300;font-size:10px;color:#777;line-height:24px;letter-spacing:.3px}

.about{left:51px}
.about .lead{font-size:12px;color:var(--red);line-height:16px;margin-top:13px}
.about p{font-family:"Lora",serif;font-style:italic;font-size:11px;line-height:16.5px;color:var(--ink);margin:14px 18px 0}
.about .photo{position:absolute;left:14px;top:178px;width:193px;height:108px;background:linear-gradient(90deg,#efe9dd 0%,#ddd2bf 45%,#c97a84 62%,#e9e2d6 80%,#3b3b3b 100%)}

.packages{left:280px}
.packages ul{list-style:none;margin-top:22px}
.packages li{font-family:"Cinzel",serif;font-size:12.5px;color:#333;letter-spacing:.5px}
.packages li::before{content:"";display:block;width:16px;height:6px;margin:0 auto 5px;border:1px solid var(--pink);border-radius:50%}
.packages li+li{margin-top:24px}

.staff{left:508px}
.staff .slider{display:flex;justify-content:space-between;padding:0 12px;align-items:baseline}
.staff .slider span{font-size:11px;color:var(--grey)}
.staff .portrait{position:absolute;left:15px;top:47px;width:192px;height:240px;background:linear-gradient(135deg,#a4855f 0%,#7d5a3b 40%,#8b6b8e 70%,#5c4060 100%)}
.staff .person{position:absolute;left:0;right:0;top:297px;font-family:"Lora",serif;font-size:11px;line-height:16px}
.staff .person b{font-style:italic;font-weight:400;color:#333;display:block}
.staff .person i{color:#555}

.tips{left:743px;top:542px;width:185px}
.tips a{display:block;height:59.5px;background:var(--red);border-bottom:1px solid var(--red-line);color:var(--white);text-decoration:none;text-align:center;display:flex;flex-direction:column;justify-content:center}
.tips a:last-child{border-bottom:0}
.tips strong{font-family:"Lora",serif;font-style:italic;font-weight:400;font-size:11.5px;line-height:14px}
.tips small{font-size:8.5px;letter-spacing:.5px;margin-top:3px}

.testimonials{left:743px;top:785px;width:185px;height:159px;background:var(--pale);text-align:center;font-family:"Lora",serif}
.testimonials .head{display:flex;justify-content:space-between;padding:12px 12px 0;align-items:baseline}
.testimonials .head span{font-family:"Lato",sans-serif;font-size:11px;color:var(--grey)}
.testimonials .head a{color:var(--red);font-size:12.5px}
.testimonials .date{font-family:"Lato",sans-serif;font-size:11px;color:#555;margin-top:10px}
.testimonials p{font-style:italic;font-size:11px;line-height:16px;color:#555;margin-top:2px}
.testimonials .btn{position:absolute;left:10px;right:10px;bottom:10px;height:24px;background:var(--white);font-family:"Lato",sans-serif;font-weight:300;font-size:9.5px;color:#777;line-height:24px}

.contact{left:743px;top:950px;width:185px;height:49px;background:var(--dark);color:var(--white);text-align:center;padding-top:9px}
.contact strong{display:block;font-family:"Lora",serif;font-style:italic;font-size:11.5px}
.contact span{font-size:9.5px;letter-spacing:.3px}

.site-footer{left:0;top:1092px;width:979px;height:28px;background:var(--pale);font-weight:300;font-size:9.5px;color:#777;display:flex;align-items:center;gap:14px;padding-left:50px}
</style>
</head>
<body>

<div class="abs shortlist-bar">
  <span class="label">Sign up to the Shortlist</span>
  <span class="email">enter email</span>
  <span class="social"><span></span><span></span><span></span><span></span></span>
</div>

<nav class="abs main-nav">
  <span>ABOUT</span><span>CLIENTS</span><span>CANDIDATES</span><span>SERVICES</span><span>CLASSIQUE</span><span>ELITE &amp; ROYAL</span><span>DESIGNERS</span><span>MEDIA</span><span>CONTACT</span>
</nav>

<div class="abs brand">
  <div class="mark"></div>
  <div class="name">MAISON ORÉLIE</div>
  <div class="sub">PREMIUM DOMESTIC</div>
</div>

<p class="abs tagline">Premium domestic company delivering high-caliber professionals to suit even the most demanding, challenging and refined household tasks.</p>

<div class="abs hero" role="img" aria-label="Photograph of a cream-coloured palace under blue sky with red roses in the foreground"><div class="blooms"></div></div>

<section class="abs seeking">
  <h2>ARE YOU LOOKING FOR...</h2>
  <ul>
    <li>CAREER NANNIES</li><li>ETIQUETTE GOVERNESSES</li><li>ROYAL PROTOCOL ATTENDEES</li><li>FORMAL PALACE PERSONNEL</li>
  </ul>
  <ul style="margin-top:0">
    <li>OFFICIAL BUTLER</li><li>WORLD CLASS CHEFS</li><li>SKILLED HOUSEKEEPERS</li><li>EXPERIENCED BABYNURSES</li><li>DOMESTIC COUPLES</li>
  </ul>
  <ul style="margin-top:0">
    <li>GOURMET COOKS</li><li>PERSONAL BEAUTICIAN</li><li>PROFESSIONAL LAUNDRESSES</li><li>ENTHUSIASTIC CHAUFFEURS</li>
  </ul>
</section>

<section class="abs card about">
  <h2>ABOUT US</h2>
  <div class="lead">LOREM IPSUM DOLOR SIT AMET<br>CONSECTETUR ADIPISICI ELIT</div>
  <p>Lorem ipsum dolor sit amet, consectetur adipisici elit, sed eiusmod tempor incidunt ut labore et dolore magna aliqu enim ad minim veniam, quis nostrud exercitatio.</p>
  <div class="photo" role="img" aria-label="Photograph of an elegant hallway with a pink chair and a curved staircase"></div>
  <div class="btn">CONTINUE READING</div>
</section>

<section class="abs card packages">
  <h2>PACKAGES</h2>
  <ul>
    <li>CLASSIQUE</li><li>MODA-MAISON</li><li>SOCIALITE</li><li>ELITE</li><li>ROYAL</li>
  </ul>
  <div class="btn">LEARN MORE</div>
</section>

<section class="abs card staff">
  <div class="slider"><span>&lt;</span><h2>OUR STAFF</h2><span>&gt;</span></div>
  <div class="portrait" role="img" aria-label="Photograph of a staff member in a patterned dress standing in a doorway"></div>
  <div class="person"><b>Clara Ventimiglia</b><i>Lorem Ipsum sit Doles</i></div>
</section>

<nav class="abs tips">
  <a href="#"><strong>Everyday<br>Etiquettes &amp; Courtesies</strong><small>LEARN MORE</small></a>
  <a href="#"><strong>Table Setting Etiquettes</strong><small>LEARN MORE</small></a>
  <a href="#"><strong>Etiquettes for Kids</strong><small>LEARN MORE</small></a>
  <a href="#"><strong>Tea Time Etiquette</strong><small>LEARN MORE</small></a>
</nav>

<section class="abs testimonials">
  <div class="head"><span>&lt;</span><a href="#">Testimonials</a><span>&gt;</span></div>
  <div class="date">09. OCTOBER, 2013</div>
  <p>Awesome work. It's reaselly<br>a treat that you showed<br>process for creating ame...</p>
  <div class="btn">CONTINUE READING</div>
</section>

<div class="abs contact">
  <strong>Contact us today!</strong>
  <span>INFO@MAISONORELIE.EXAMPLE</span>
</div>

<footer class="abs site-footer">
  <span>PRIVACY POLICY</span><span>LEGAL</span><span>©MAISON ORÉLIE 2013</span>
</footer>

</body>
</html>
```